Boutique town planning business needs a Business Card design

We need a business card design for a new company called The Zoning Bridgeway. We provide town planning and urban design services to government, business and community groups. We would like to see the designs use the colours in the logo (blue, deep red, green and amber), plenty of white and including black and grey in the writing. The final design should communicate collaboration, creativity and professionalism and that we are approachable.

Industry/Entity Type

Town

```html
<!DOCTYPE html>
<html lang="en">
<head>
<meta charset="utf-8">
<title>The Zoning Bridgeway – Business Card</title>
<link rel="stylesheet" href="https://fonts.googleapis.com/css2?family=Arimo:wght@400;700&display=swap">
<style>
  :root {
    --page: #e9e7e3;
    --card-white: #ffffff;
    --card-black: #161616;
    --pattern-dark: #1f1f1f;
    --ink: #111111;
    --ink-grey: #5a5d62;
    --brand-grey: #2b2b2b;
    --blue: #1f8fc4;
    --green: #5aaa3c;
    --amber: #f0961e;
    --red: #c4302b;
    --faint-blue: #cfe2ee;
  }
  * { margin: 0; padding: 0; box-sizing: border-box; }
  html, body {
    width: 1200px; height: 1000px; overflow: hidden;
    background: var(--page);
    font-family: "Arimo", Arial, sans-serif;
  }
  .stage {
    width: 1200px; height: 1000px;
    display: flex; flex-direction: column; align-items: center; justify-content: center;
    gap: 44px;
  }
  .card {
    position: relative;
    width: 700px; height: 400px;
    box-shadow: 0 6px 18px rgba(0,0,0,.18);
    overflow: hidden;
  }
  /* Back */
  .card-back { background: var(--card-black); }
  .back-pattern {
    position: absolute; inset: 0;
    background: radial-gradient(circle at 50% 50%, var(--pattern-dark), var(--card-black) 75%);
  }
  .back-brand {
    position: absolute; left: 50%; top: 50%; transform: translate(-50%, -50%);
    display: flex; align-items: center; gap: 14px;
  }
  .back-brand .brand-dot { width: 38px; height: 38px; background: var(--blue); }
  .back-brand .brand-name { color: #ffffff; }
  /* Brand lockup */
  .brand-dot { border-radius: 50%; flex: none; }
  .brand-name { font-weight: 700; font-size: 28px; letter-spacing: -0.3px; color: var(--brand-grey); white-space: nowrap; }
  /* Front */
  .card-front { background: var(--card-white); }
  .watermark-circle {
    position: absolute; left: 4px; top: 214px;
    width: 176px; height: 176px; border-radius: 50%;
    background: var(--faint-blue); opacity: .7;
  }
  .person { position: absolute; left: 42px; top: 98px; width: 250px; }
  .person-name { font-weight: 700; font-size: 22px; color: var(--ink); margin-bottom: 4px; }
  .person-credentials { font-size: 16px; line-height: 1.25; color: var(--ink-grey); }
  .person-title { font-size: 18px; color: var(--blue); margin-top: 2px; }
  .front-brand {
    position: absolute; right: 46px; top: 14px;
    display: flex; flex-direction: column; align-items: flex-end;
  }
  .front-brand .brand-dot {
    width: 112px; height: 112px; background: var(--green);
    margin-right: 60px; margin-bottom: 12px;
  }
  .abn { font-size: 13px; color: var(--ink); margin-top: 4px; }
  .contacts {
    position: absolute; right: 34px; bottom: 40px;
    list-style: none; text-align: right;
    font-size: 16.5px; color: var(--ink-grey); line-height: 25px;
  }
  .contacts li { display: flex; align-items: center; justify-content: flex-end; gap: 8px; }
  .contacts svg { width: 16px; height: 16px; flex: none; }
</style>
</head>
<body>
<main class="stage">
  <section class="card card-back" aria-label="Business card back">
    <div class="back-pattern" role="img" aria-label="Dark repeating tile pattern across the card back"></div>
    <div class="back-brand">
      <span class="brand-dot"></span>
      <span class="brand-name">The Zoning Bridgeway</span>
    </div>
  </section>

  <section class="card card-front" aria-label="Business card front">
    <div class="watermark-circle"></div>

    <div class="person">
      <p class="person-name">Marian Holloway</p>
      <p class="person-credentials">BEnvD (Town Design), GCertUS,<br>MZPS, RPCA</p>
      <p class="person-title">Director</p>
    </div>

    <div class="front-brand">
      <span class="brand-dot"></span>
      <span class="brand-name">The Zoning Bridgeway</span>
      <p class="abn">ABN 10293847561</p>
    </div>

    <ul class="contacts">
      <li>0400 555 218
        <svg viewBox="0 0 16 16" aria-hidden="true"><rect x="4" y="1" width="8" height="14" rx="1.5" fill="none" stroke="var(--green)" stroke-width="1.6"/><rect x="6" y="3" width="4" height="6" fill="var(--green)"/></svg>
      </li>
      <li>hello@zoningbridgeway.net
        <svg viewBox="0 0 16 16" aria-hidden="true"><rect x="1" y="3" width="14" height="10" fill="var(--amber)"/><path d="M1 3 L8 9 L15 3" fill="none" stroke="#fff" stroke-width="1.4"/></svg>
      </li>
      <li>www.zoningbridgeway.com.au
        <svg viewBox="0 0 16 16" aria-hidden="true"><circle cx="8" cy="8" r="7" fill="var(--red)"/><path d="M1 8 H15 M8 1 C4 5 4 11 8 15 M8 1 C12 5 12 11 8 15" fill="none" stroke="#fff" stroke-width="1"/></svg>
      </li>
    </ul>
  </section>
</main>
</body>
</html>
```